Digital Marketing company needs business cards

We are a digital marketing company providing SEO, Bidlane and Web Development services in Australia and New Zealand. Colours and icons have to match the current website (kestrelworks.com.au). We'd like to keep the cards simple and clean, using the artwork we have as the background of the slider of the website (the triangles). The card should have horizontal layout.
If we could have our core services on the reverse side that'd be great:
SEO
BidLane
Web Design&Development
Target Market(s)
Medium size to large businesses
Industry/Entity Type
Digital

```html
<!DOCTYPE html>
<html lang="en">
<head>
<meta charset="utf-8">
<title>kestrelworks business card</title>
<link rel="stylesheet" href="https://fonts.googleapis.com/css2?family=Open+Sans:wght@400;600;700&display=swap">
<style>
  :root {
    --backdrop: #e4e5e6;
    --card: #ffffff;
    --card-edge: #d9dbdd;
    --brand-blue: #1a8cbf;
    --ink: #3a3d40;
    --ink-soft: #4a4e52;
    --rule: #55595d;
  }
  * { box-sizing: border-box; margin: 0; padding: 0; }
  html, body {
    width: 1200px;
    height: 1026px;
    overflow: hidden;
    background: var(--backdrop);
    font-family: "Open Sans", Arial, sans-serif;
  }
  .sheet {
    width: 1200px;
    height: 1026px;
    display: flex;
    flex-direction: column;
    align-items: center;
    justify-content: center;
    gap: 56px;
  }
  .card {
    position: relative;
    width: 760px;
    height: 434px;
    background: var(--card);
    border: 1px solid var(--card-edge);
    box-shadow: 0 2px 6px rgba(0,0,0,0.08);
    overflow: hidden;
  }
  .wordmark {
    position: absolute;
    display: flex;
    align-items: center;
    gap: 10px;
    font-weight: 600;
    color: var(--brand-blue);
    letter-spacing: -0.5px;
    white-space: nowrap;
  }
  .wordmark .dot {
    border-radius: 50%;
    background: var(--brand-blue);
    flex: none;
  }

  /* back */
  .card-back .wordmark {
    left: 190px;
    top: 168px;
    font-size: 38px;
  }
  .card-back .wordmark .dot { width: 30px; height: 30px; }
  .card-back .divider {
    position: absolute;
    left: 560px;
    top: 70px;
    width: 1px;
    height: 300px;
    background: var(--rule);
  }

  /* front */
  .card-front .accent-band {
    position: absolute;
    left: 34px;
    top: 0;
    width: 11px;
    height: 100%;
    background: var(--brand-blue);
  }
  .card-front .wordmark {
    left: 96px;
    top: 84px;
    font-size: 54px;
  }
  .card-front .wordmark .dot { width: 40px; height: 40px; }
  .contact {
    position: absolute;
    left: 82px;
    top: 256px;
  }
  .contact-title {
    font-size: 22px;
    font-weight: 700;
    color: var(--ink);
    margin-bottom: 10px;
  }
  .contact-title .lead { color: var(--brand-blue); }
  .contact-list { list-style: none; }
  .contact-list li {
    display: flex;
    align-items: center;
    gap: 10px;
    font-size: 18px;
    color: var(--ink-soft);
    line-height: 28px;
  }
  .contact-list svg { width: 14px; height: 14px; flex: none; }
</style>
</head>
<body>
<main class="sheet">

  <section class="card card-back" aria-label="Business card, back">
    <div class="wordmark"><span class="dot"></span>kestrelworks</div>
    <div class="divider"></div>
  </section>

  <section class="card card-front" aria-label="Business card, front">
    <div class="accent-band"></div>
    <div class="wordmark"><span class="dot"></span>kestrelworks</div>
    <div class="contact">
      <h2 class="contact-title"><span class="lead">Contact</span> Me</h2>
      <ul class="contact-list">
        <li>
          <svg viewBox="0 0 16 16" aria-hidden="true"><path d="M4 1.5c1 0 1.6 2.6 1.6 3.3 0 .8-1.2 1.1-1 2 .4 1.6 2.2 3.6 3.6 4 .8.2 1.2-.9 2-.9.8 0 3.3.7 3.3 1.7 0 1-1.3 2.6-2.6 2.6C6 14.2 1.8 9.9 1.8 4 1.8 2.7 3 1.5 4 1.5z" fill="var(--brand-blue)"/></svg>
          021 483 5907
        </li>
        <li>
          <svg viewBox="0 0 16 16" aria-hidden="true"><rect x="1" y="3" width="14" height="10" rx="1" fill="var(--brand-blue)"/><path d="M1.5 3.8 8 9l6.5-5.2" fill="none" stroke="#fff" stroke-width="1.3"/></svg>
          hello@kestrelworks.com.au
        </li>
        <li>
          <svg viewBox="0 0 16 16" aria-hidden="true"><circle cx="8" cy="8" r="6.5" fill="none" stroke="var(--brand-blue)" stroke-width="1.6"/><ellipse cx="8" cy="8" rx="2.6" ry="6.5" fill="none" stroke="var(--brand-blue)" stroke-width="1.2"/><path d="M1.5 8h13" stroke="var(--brand-blue)" stroke-width="1.2"/></svg>
          www.kestrelworks.com.au
        </li>
      </ul>
    </div>
  </section>

</main>
</body>
</html>
```